BRAVO Property Concierge

We require a website built for this company. Logo is also on the attached document. Some info on the company:<br/>To create a work class experience for our clients for property maintenance. A personalised service that deliver’s what landlords need...Quality work, on time and managed from start to finish.<br/>We do things different, our clients deal with one contact, a client manager who manages your maintenance task from start to finish. Our service allows our expert trades people to do what they do best and leave the management/organising to us!<br/>I have drafted up the layout of the web ... very brief at this stage however once we have more info we will add links and can collate more information and provide. <br/>We just want to get a layout of what you think the web should look like and can go from there.

```html
<!DOCTYPE html>
<html lang="en">
<head>
<meta charset="utf-8">
<title>BRAVO Property Concierge</title>
<link href="https://fonts.googleapis.com/css2?family=Lato:wght@300;400;700;900&display=swap" rel="stylesheet">
<style>
:root{
  --yellow:#fcb711;
  --yellow-dark:#f3a500;
  --ink:#222222;
  --text:#4a4a4a;
  --muted:#777777;
  --charcoal:#333333;
  --footer:#2b2b2b;
  --white:#ffffff;
  --line:#e3e3e3;
}
*{box-sizing:border-box;margin:0;padding:0}
html,body{width:1200px;height:4161px;overflow:hidden;background:var(--white)}
body{font-family:'Lato',sans-serif;color:var(--text)}
.page{position:relative;width:1200px;height:4161px;overflow:hidden}
.abs{position:absolute}
.btn{position:absolute;display:flex;align-items:center;justify-content:center;font-weight:700;text-transform:uppercase;color:var(--ink);background:var(--yellow)}

/* header */
.site-header{position:absolute;left:0;top:0;width:1200px;height:94px;background:var(--white);border-bottom:1px solid var(--line)}
.brand{position:absolute;left:152px;top:14px;line-height:1}
.brand-name{font-size:50px;font-weight:400;color:var(--ink);letter-spacing:-1px}
.brand-sub{font-size:12px;font-weight:700;color:var(--ink);letter-spacing:.3px;margin-top:1px}
.nav{position:absolute;top:27px;left:466px;display:flex;gap:0}
.nav a{display:flex;align-items:center;height:43px;font-size:15px;color:var(--ink);text-decoration:none;padding:0 22px}
.nav a.active{border:3px solid var(--yellow)}
.social-mini{position:absolute;top:38px;display:flex;gap:34px;left:940px}
.social-mini span{width:16px;height:16px;border-radius:50%;background:var(--ink);display:block}

/* hero */
.hero-title{position:absolute;left:0;width:1200px;text-align:center;color:var(--white)}
.hero-title.big{top:356px;font-size:49px;font-weight:900;letter-spacing:-.5px}
.hero-title.sub{top:412px;font-size:50px;font-weight:300}

/* about */
.section-title{position:absolute;left:0;width:1200px;text-align:center;font-weight:900;text-transform:uppercase}
.about-title{top:852px;font-size:36px;color:var(--ink)}
.about-title::after{content:"";display:block;width:56px;height:3px;background:var(--yellow);margin:8px auto 0}
.about-copy{position:absolute;top:930px;left:220px;width:760px;text-align:center;font-size:18px;line-height:31px;color:var(--text)}
.member{position:absolute;width:240px;text-align:center}
.member svg{display:block;margin:0 auto}
.member h3{font-size:19px;font-weight:700;color:var(--ink);margin-top:24px}
.member p{font-size:11px;line-height:14px;color:var(--text);margin-top:6px}
.member .bio-btn{position:relative;display:inline-flex;margin-top:12px;width:88px;height:28px;font-size:10px;background:var(--yellow);color:var(--white);font-weight:700;align-items:center;justify-content:center}

/* services */
.services-title{top:1570px;font-size:28px;color:var(--white)}
.service-card{position:absolute;top:1684px;width:270px;height:256px;background:var(--white);text-align:center}
.service-card.featured{background:var(--charcoal)}
.service-card h3{margin-top:84px;font-size:18px;font-weight:900;color:var(--ink)}
.service-card p{margin:8px auto 0;width:230px;font-size:11px;line-height:19px;color:var(--text)}
.service-card .outline-btn{display:inline-flex;align-items:center;justify-content:center;margin-top:16px;width:136px;height:39px;border:2px solid var(--yellow);font-size:12px;font-weight:700;color:var(--ink)}
.service-card.featured h3,.service-card.featured p,.service-card.featured .outline-btn{color:var(--white)}
.service-icon{position:absolute;left:73px;top:-62px}
.arrow{position:absolute;top:1790px}

/* benefit */
.benefit-title{position:absolute;left:157px;top:2186px;font-size:30px;font-weight:900;color:var(--ink)}
.benefit-copy{position:absolute;left:157px;top:2235px;width:430px;font-size:17px;line-height:31px;color:var(--text)}
.benefit-list{position:absolute;left:157px;top:2322px;display:grid;grid-template-columns:220px 220px;row-gap:10px;list-style:none}
.benefit-list li{display:flex;align-items:center;gap:10px;font-size:17px;font-weight:700;color:var(--text);height:23px}

/* quote */
.quote-title{top:2680px;font-size:28px;color:var(--white)}
.field{position:absolute;border:1px solid #8a8a8a;color:#cfcfcf;font-size:14px;padding:16px 20px;text-transform:uppercase;background:rgba(255,255,255,.02)}

/* blogs */
.blogs-title{position:absolute;left:165px;top:3160px;font-size:30px;font-weight:900;color:var(--ink)}
.meta{font-size:12px;color:var(--muted);font-weight:700}
.meta span{font-weight:400}
.post-title{font-size:17px;font-weight:700;color:var(--ink);line-height:24px;text-transform:uppercase}
.more{font-size:15px;font-weight:700;color:var(--yellow)}
.post-side{position:absolute;left:788px;width:260px}
.rule{position:absolute;left:628px;width:420px;height:1px;background:#d6d6d6}

/* footer */
.site-footer{position:absolute;left:0;top:3762px;width:1200px;height:399px;background:var(--footer);color:#cfcfcf}
.footer-brand{position:absolute;left:170px;top:58px;line-height:1}
.footer-brand .brand-name{color:var(--white);font-size:48px}
.footer-brand .brand-sub{color:var(--white)}
.footer-about{position:absolute;left:170px;top:156px;width:230px;font-size:13px;line-height:22px}
.footer-col{position:absolute;top:76px}
.footer-col h4{font-size:16px;font-weight:700;color:var(--white);text-transform:uppercase;margin-bottom:18px}
.footer-col li{list-style:none;font-size:13px;line-height:27px}
.contact-row{display:flex;gap:10px;font-size:13px;line-height:17px;margin-bottom:14px;align-items:flex-start}
.social-row{display:flex;align-items:center;gap:10px;font-size:13px;text-transform:uppercase;height:34px}
.social-row i{width:26px;height:26px;border-radius:50%;background:var(--white);display:block}
.copyright{position:absolute;left:0;top:344px;width:1200px;text-align:center;font-size:14px;color:#bdbdbd}
</style>
</head>
<body>
<div class="page">

  <!-- Hero -->
  <svg class="abs" style="left:0;top:94px" width="1200" height="700" viewBox="0 0 1200 700">
    <defs>
      <linearGradient id="sky" x1="0" y1="0" x2="0" y2="1">
        <stop offset="0" stop-color="#3b4a63"/>
        <stop offset=".35" stop-color="#7d6a6a"/>
        <stop offset=".55" stop-color="#c88a5c"/>
        <stop offset=".75" stop-color="#3a3432"/>
        <stop offset="1" stop-color="#1d1b1a"/>
      </linearGradient>
    </defs>
    <rect width="1200" height="700" fill="url(#sky)" role="img" aria-label="City skyline at dusk with towers under a dramatic sunset sky"/>
    <rect width="1200" height="700" fill="rgba(0,0,0,.18)"/>
    <polygon points="0,582 600,676 1200,582 1200,700 0,700" fill="var(--yellow)"/>
    <polygon points="0,596 600,676 1200,596 1200,602 600,690 0,602" fill="var(--yellow)"/>
    <polygon points="0,604 600,700 1200,604 1200,700 0,700" fill="var(--white)"/>
    <polygon points="0,582 600,676 1200,582 1200,604 600,700 0,604" fill="var(--yellow)"/>
    <circle cx="598" cy="209" r="39" fill="var(--white)"/>
    <polygon points="588,191 613,209 588,227" fill="var(--ink)"/>
  </svg>

  <header class="site-header">
    <div class="brand">
      <div class="brand-name">BRAVO</div>
      <div class="brand-sub">PROPERTY CONCIERGE</div>
    </div>
    <nav class="nav">
      <a class="active" href="#">HOME</a>
      <a href="#">ABOUT US</a>
      <a href="#">SERVICES</a>
      <a href="#">BENEFITS</a>
    </nav>
    <div class="social-mini"><span></span><span></span><span></span></div>
  </header>

  <h1 class="hero-title big">WELCOME TO BRAVO</h1>
  <p class="hero-title sub">BRAVO PROPERTY CONCIERGE</p>
  <div class="btn" style="left:512px;top:485px;width:176px;height:52px;font-size:17px">Learn More</div>

  <!-- About -->
  <h2 class="section-title about-title">About Bravo</h2>
  <p class="about-copy">Fusce tellus Sed metus augue convallis et vehicula ut pulvinar eu ante Integer orci tellus tristique vitae consequat nec porta vel lectus Nulla sit amet aliquam enim Proin dui lectus cursus eu mattis laoreet viverra sit amet quam Curabitur vel dolor</p>

  <svg class="abs" style="left:0;top:1230px" width="1200" height="350" viewBox="0 0 1200 350" aria-hidden="true">
    <rect width="1200" height="350" fill="#f7f7f7" opacity=".6"/>
  </svg>

  <div class="member" style="left:195px;top:1072px">
    <svg width="212" height="240" viewBox="0 0 212 240"><defs><linearGradient id="p1" x1="0" y1="0" x2="0" y2="1"><stop offset="0" stop-color="#ececec"/><stop offset="1" stop-color="#2a2a2a"/></linearGradient></defs><polygon points="106,0 212,60 212,180 106,240 0,180 0,60" fill="url(#p1)" role="img" aria-label="Portrait of team member Owen Marsh"/></svg>
    <h3>OWEN MARSH</h3>
    <p>Lorem ipsum dolor sit amet consectetuer<br>adipiscing elit Nam cursus Morbi ut</p>
    <span class="bio-btn">VIEW BIO</span>
  </div>
  <div class="member" style="left:487px;top:1077px">
    <svg width="212" height="240" viewBox="0 0 212 240"><defs><linearGradient id="p2" x1="0" y1="0" x2="0" y2="1"><stop offset="0" stop-color="#c9d0d2"/><stop offset="1" stop-color="#1f2535"/></linearGradient></defs><polygon points="106,0 212,60 212,180 106,240 0,180 0,60" fill="url(#p2)" role="img" aria-label="Portrait of team member Leo Harding"/></svg>
    <h3>LEO HARDING</h3>
    <p>Lorem ipsum dolor sit amet consectetuer<br>adipiscing elit Nam cursus</p>
    <span class="bio-btn">VIEW BIO</span>
  </div>
  <div class="member" style="left:782px;top:1077px">
    <svg width="212" height="240" viewBox="0 0 212 240"><defs><linearGradient id="p3" x1="0" y1="0" x2="0" y2="1"><stop offset="0" stop-color="#e8e8e8"/><stop offset="1" stop-color="#1b1b1b"/></linearGradient></defs><polygon points="106,0 212,60 212,180 106,240 0,180 0,60" fill="url(#p3)" role="img" aria-label="Portrait of team member Clara Wendt"/></svg>
    <h3>CLARA WENDT</h3>
    <p>Lorem ipsum dolor sit amet consectetuer<br>adipiscing elit Nam cursus</p>
    <span class="bio-btn">VIEW BIO</span>
  </div>

  <!-- Services band -->
  <svg class="abs" style="left:0;top:1500px" width="1200" height="600" viewBox="0 0 1200 600" aria-hidden="true">
    <polygon points="0,90 600,0 1200,90 1200,515 600,600 0,515" fill="var(--yellow)"/>
  </svg>
  <h2 class="section-title services-title">Our Services</h2>

  <svg class="arrow" style="left:114px" width="20" height="36" viewBox="0 0 20 36"><polyline points="17,3 3,18 17,33" fill="none" stroke="#fff" stroke-width="3"/></svg>
  <svg class="arrow" style="left:1052px" width="20" height="36" viewBox="0 0 20 36"><polyline points="3,3 17,18 3,33" fill="none" stroke="#fff" stroke-width="3"/></svg>

  <div class="service-card" style="left:176px">
    <svg class="service-icon" width="124" height="124" viewBox="0 0 124 124"><polygon points="62,2 122,62 62,122 2,62" fill="#fff" stroke="var(--yellow)" stroke-width="6"/><rect x="44" y="44" width="36" height="26" fill="none" stroke="#222" stroke-width="2"/><line x1="52" y1="64" x2="52" y2="56" stroke="#222" stroke-width="3"/><line x1="59" y1="64" x2="59" y2="51" stroke="#222" stroke-width="3"/><line x1="66" y1="64" x2="66" y2="54" stroke="#222" stroke-width="3"/><line x1="73" y1="64" x2="73" y2="49" stroke="#222" stroke-width="3"/><line x1="54" y1="78" x2="70" y2="78" stroke="#222" stroke-width="2"/></svg>
    <h3>TRADE PEOPLE</h3>
    <p>Lorem ipsum dolor sit amet consectetuer adipiscing elit Nam cursus Morbi ut mi Nullam enim leo</p>
    <span class="outline-btn">LEARN MORE</span>
  </div>
  <div class="service-card featured" style="left:464px">
    <svg class="service-icon" width="124" height="124" viewBox="0 0 124 124"><polygon points="62,2 122,62 62,122 2,62" fill="var(--charcoal)" stroke="#222" stroke-width="6"/><g fill="none" stroke="#fff" stroke-width="2"><circle cx="62" cy="62" r="6"/><circle cx="48" cy="46" r="4"/><circle cx="77" cy="46" r="4"/><circle cx="46" cy="76" r="4"/><circle cx="78" cy="77" r="4"/><line x1="57" y1="57" x2="51" y2="49"/><line x1="67" y1="57" x2="74" y2="49"/><line x1="57" y1="67" x2="49" y2="73"/><line x1="67" y1="67" x2="75" y2="74"/></g></svg>
    <h3>CONNECTIONS</h3>
    <p>Lorem ipsum dolor sit amet consectetuer adipiscing elit Nam cursus Morbi ut mi Nullam enim leo</p>
    <span class="outline-btn">LEARN MORE</span>
  </div>
  <div class="service-card" style="left:752px">
    <svg class="service-icon" width="124" height="124" viewBox="0 0 124 124"><polygon points="62,2 122,62 62,122 2,62" fill="#fff" stroke="var(--yellow)" stroke-width="6"/><g fill="none" stroke="#222" stroke-width="2"><rect x="50" y="42" width="24" height="22" transform="rotate(-12 62 53)"/><line x1="56" y1="58" x2="68" y2="47"/><circle cx="57" cy="49" r="2"/><circle cx="67" cy="57" r="2"/><path d="M42 74 q10 -6 22 0 h12 q4 0 0 4 h-14"/><path d="M42 82 h28 l12 -10"/></g></svg>
    <h3>FINANCE</h3>
    <p>Lorem ipsum dolor sit amet consectetuer adipiscing elit Nam cursus Morbi ut mi Nullam enim leo</p>
    <span class="outline-btn">LEARN MORE</span>
  </div>

  <!-- Benefit -->
  <svg class="abs" style="left:430px;top:2020px" width="770" height="640" viewBox="0 0 770 640">
    <defs>
      <linearGradient id="couple" x1="0" y1="0" x2="1" y2="0">
        <stop offset="0" stop-color="#ffffff"/>
        <stop offset=".25" stop-color="#eef0f2"/>
        <stop offset=".6" stop-color="#c7cfdb"/>
        <stop offset="1" stop-color="#e6e2dc"/>
      </linearGradient>
    </defs>
    <rect width="770" height="640" fill="url(#couple)" role="img" aria-label="Smiling couple sitting on the floor of their living room sharing a laptop"/>
  </svg>
  <svg class="abs" style="left:0;top:2010px" width="1200" height="100" viewBox="0 0 1200 100" aria-hidden="true">
    <polygon points="0,0 1200,0 1200,5 600,90 0,5" fill="var(--yellow)"/>
  </svg>
  <h2 class="benefit-title">BENEFIT WITH BRAVO</h2>
  <p class="benefit-copy">Fusce tellus Sed metus augue convallis et vehicula ut pulvinar eu ante Integer orci tellus tristique</p>
  <ul class="benefit-list">
    <li><svg width="17" height="17" viewBox="0 0 17 17"><circle cx="8.5" cy="8.5" r="7" fill="none" stroke="#777" stroke-width="1.5"/><polyline points="5,9 8,12 14,4" fill="none" stroke="#777" stroke-width="1.5"/></svg>Customer service</li>
    <li><svg width="17" height="17" viewBox="0 0 17 17"><circle cx="8.5" cy="8.5" r="7" fill="none" stroke="#777" stroke-width="1.5"/><polyline points="5,9 8,12 14,4" fill="none" stroke="#777" stroke-width="1.5"/></svg>Pricing</li>
    <li><svg width="17" height="17" viewBox="0 0 17 17"><circle cx="8.5" cy="8.5" r="7" fill="none" stroke="#777" stroke-width="1.5"/><polyline points="5,9 8,12 14,4" fill="none" stroke="#777" stroke-width="1.5"/></svg>Call centre</li>
    <li><svg width="17" height="17" viewBox="0 0 17 17"><circle cx="8.5" cy="8.5" r="7" fill="none" stroke="#777" stroke-width="1.5"/><polyline points="5,9 8,12 14,4" fill="none" stroke="#777" stroke-width="1.5"/></svg>Level of expertise</li>
    <li><svg width="17" height="17" viewBox="0 0 17 17"><circle cx="8.5" cy="8.5" r="7" fill="none" stroke="#777" stroke-width="1.5"/><polyline points="5,9 8,12 14,4" fill="none" stroke="#777" stroke-width="1.5"/></svg>Values</li>
  </ul>
  <div class="btn" style="left:160px;top:2444px;width:170px;height:50px;font-size:16px">Learn More</div>

  <!-- Quote -->
  <svg class="abs" style="left:0;top:2584px" width="1200" height="520" viewBox="0 0 1200 520" aria-hidden="true">
    <polygon points="0,78 600,0 1200,78 1200,436 600,516 0,436" fill="var(--charcoal)"/>
  </svg>
  <h2 class="section-title quote-title">Request a Quote</h2>
  <div class="field" style="left:195px;top:2748px;width:393px;height:48px">Name</div>
  <div class="field" style="left:195px;top:2808px;width:393px;height:48px">Email</div>
  <div class="field" style="left:195px;top:2868px;width:393px;height:48px">Phone</div>
  <div class="field" style="left:600px;top:2748px;width:393px;height:168px">Message</div>
  <div class="btn" style="left:489px;top:2943px;width:196px;height:52px;font-size:17px">Submit Now</div>

  <!-- Blogs -->
  <h2 class="blogs-title">RECENT BLOGS</h2>
  <svg class="abs" style="left:162px;top:3230px" width="429" height="242" viewBox="0 0 429 242"><defs><linearGradient id="b1" x1="0" y1="0" x2="0" y2="1"><stop offset="0" stop-color="#4f8fd6"/><stop offset=".55" stop-color="#29457a"/><stop offset="1" stop-color="#4e8d3a"/></linearGradient></defs><rect width="429" height="242" fill="url(#b1)" role="img" aria-label="Blue two-storey family house with a front lawn"/></svg>
  <div class="abs" style="left:172px;top:3502px;width:400px">
    <div class="meta">April 12, 2019 &nbsp;|&nbsp; <span>No Comments</span></div>
    <div class="post-title" style="margin-top:12px">Mauris vel lacus vitae felis vestibulum volutpat etiam est nunc</div>
    <p style="font-size:12px;line-height:20px;margin-top:14px">Nunc tempus felis vitae urna Vivamus porttitor neque at volutpat rutrum purus nisi eleifend libero a tempus libero lectus</p>
    <div class="more" style="margin-top:14px">LEARN MORE</div>
  </div>

  <svg class="abs" style="left:628px;top:3230px" width="143" height="118" viewBox="0 0 143 118"><defs><linearGradient id="b2" x1="0" y1="0" x2="0" y2="1"><stop offset="0" stop-color="#7fb1e3"/><stop offset=".6" stop-color="#c9bca5"/><stop offset="1" stop-color="#5d8f3c"/></linearGradient></defs><rect width="143" height="118" fill="url(#b2)" role="img" aria-label="Suburban house with a green lawn"/></svg>
  <div class="post-side" style="top:3241px">
    <div class="meta">April 08, 2019 &nbsp;|&nbsp; <span>No Comments</span></div>
    <div class="post-title" style="margin-top:6px">Mauris vel lacus vitae felis vestibulum volutpat</div>
    <div class="more" style="margin-top:8px">LEARN MORE</div>
  </div>
  <div class="rule" style="top:3360px"></div>

  <svg class="abs" style="left:630px;top:3390px" width="143" height="118" viewBox="0 0 143 118"><defs><linearGradient id="b3" x1="0" y1="0" x2="0" y2="1"><stop offset="0" stop-color="#3e6fb8"/><stop offset=".6" stop-color="#6d6a66"/><stop offset="1" stop-color="#8a8a80"/></linearGradient></defs><rect width="143" height="118" fill="url(#b3)" role="img" aria-label="Stone-fronted house under a blue sky"/></svg>
  <div class="post-side" style="top:3391px;left:790px">
    <div class="meta">April 06, 2019 &nbsp;|&nbsp; <span>No Comments</span></div>
    <div class="post-title" style="margin-top:6px">Fusce tellus sed metus augue convallis et</div>
    <div class="more" style="margin-top:8px">LEARN MORE</div>
  </div>
  <div class="rule" style="top:3524px"></div>

  <svg class="abs" style="left:632px;top:3550px" width="143" height="118" viewBox="0 0 143 118"><defs><linearGradient id="b4" x1="0" y1="0" x2="1" y2="1"><stop offset="0" stop-color="#d9d9d6"/><stop offset=".5" stop-color="#5a5048"/><stop offset="1" stop-color="#3d5d86"/></linearGradient></defs><rect width="143" height="118" fill="url(#b4)" role="img" aria-label="Couple reviewing paperwork at home"/></svg>
  <div class="post-side" style="top:3556px;left:792px">
    <div class="meta">April 02, 2019 &nbsp;|&nbsp; <span>No Comments</span></div>
    <div class="post-title" style="margin-top:6px">Phasellus felis dolor scelerisque a tempus</div>
    <div class="more" style="margin-top:8px">LEARN MORE</div>
  </div>

  <!-- Footer -->
  <footer class="site-footer">
    <div class="footer-brand">
      <div class="brand-name">BRAVO</div>
      <div class="brand-sub">PROPERTY CONCIERGE</div>
    </div>
    <p class="footer-about">Praesent elementum elit at tellus Curabitur metus ipsum luctus eu malesuada ut tincidunt</p>

    <div class="footer-col" style="left:444px">
      <h4>Contact Us</h4>
      <div class="contact-row"><svg width="14" height="18" viewBox="0 0 14 18"><path d="M7 1a6 6 0 0 1 6 6c0 4-6 10-6 10S1 11 1 7a6 6 0 0 1 6-6z" fill="none" stroke="#ccc" stroke-width="1.5"/><circle cx="7" cy="7" r="2" fill="none" stroke="#ccc" stroke-width="1.5"/></svg><span>48 Harlow Lane #4B<br>Fairview 20417</span></div>
      <div class="contact-row" style="font-size:16px"><svg width="14" height="16" viewBox="0 0 14 16"><path d="M3 1l3 3-2 2c1 2 3 4 5 5l2-2 3 3-2 3C6 15 0 9 1 3z" fill="none" stroke="#ccc" stroke-width="1.3"/></svg><span>(555) 014 7720</span></div>
      <div class="contact-row"><svg width="14" height="12" viewBox="0 0 14 12"><rect x="1" y="1" width="12" height="10" fill="none" stroke="#ccc" stroke-width="1.3"/><polyline points="1,1 7,7 13,1" fill="none" stroke="#ccc" stroke-width="1.3"/></svg><span>hello@bravoconcierge.example</span></div>
    </div>

    <div class="footer-col" style="left:720px">
      <h4>Company</h4>
      <ul><li>About Us</li><li>Benefits</li><li>Services</li><li>Contact Us</li></ul>
    </div>

    <div class="footer-col" style="left:902px">
      <h4>Get in Touch</h4>
      <div class="social-row"><i></i>Chirper</div>
      <div class="social-row"><i></i>Facepage</div>
      <div class="social-row"><i></i>LinkUp</div>
      <div class="social-row"><i></i>Snapgram</div>
    </div>

    <p class="copyright">Copyright © 2019 All right reserved</p>
  </footer>
</div>
</body>
</html>
```